Guided Study Tour - Halmerfest Leipzig Two Sided Flyer

We need a two-sided flyer for a Guided Study Tour to Halmerfest Leipzig. We want beautiful pictures of Germany and if possible some of the Halmer venues our participants will be visiting. I have also provided the content that needs to be included. Also, in the attached document I provided a link to the Halmerfest event. Please read and watch the video to be inspired.
This flyer should be beautiful and engaging. It needs to grab your attention right away and really highlight the wonderful things that they will be doing and that are included in the tour. This is a once in a lifetime opportunity for people to experience. We are targeting Music Directors and Music professionals.
Both attached logos need to be present on the flyer.

```html
<!DOCTYPE html>
<html lang="en">
<head>
<meta charset="utf-8">
<title>Guided Study Tour – Halmerfest Leipzig Flyer</title>
<link href="https://fonts.googleapis.com/css2?family=Kaushan+Script&family=Oswald:wght@500&family=Open+Sans:ital,wght@0,400;0,600;0,700;1,400;1,600;1,700&family=Playfair+Display:ital@1&display=swap" rel="stylesheet">
<style>
:root{
  --stage:#3b3e43;
  --paper:#ffffff;
  --red:#c8161d;
  --red-dark:#9e0f14;
  --blue:#1c4f9c;
  --ink:#2a2a2a;
  --panel:#2b2b2d;
  --muted:#bcbcbc;
  --rule:#d9d9d9;
}
*{box-sizing:border-box;margin:0;padding:0}
html,body{width:1200px;height:829px;overflow:hidden}
body{background:var(--stage);font-family:"Open Sans",Arial,sans-serif;color:var(--ink);position:relative}
.page{position:absolute;background:var(--paper);overflow:hidden;box-shadow:0 4px 14px rgba(0,0,0,.45)}
.front{left:76px;top:44px;width:497px;height:702px}
.back{left:653px;top:50px;width:494px;height:696px}
.abs{position:absolute}

/* front hero */
.hero-photo{left:0;top:0;width:497px;height:370px;
  background:linear-gradient(180deg,#6c5a93 0%,#a6839c 25%,#e2b08c 45%,#d88a4e 60%,#5b3a2e 78%,#ffffff 100%)}
.kicker{left:0;width:497px;top:14px;text-align:center;font-family:"Playfair Display",Georgia,serif;font-style:italic;font-size:17px;color:#3a2d3c}
.title{left:0;width:497px;top:30px;text-align:center;font-family:"Kaushan Script",cursive;font-size:92px;line-height:1;color:#fff;font-weight:400;text-shadow:0 2px 6px rgba(60,30,60,.35)}
.date{left:0;width:497px;top:118px;text-align:center;font-family:"Oswald",Arial,sans-serif;font-size:31px;color:#1f1f22;letter-spacing:.5px}
.place{left:0;width:497px;top:158px;text-align:center;font-style:italic;font-weight:600;font-size:13px;color:var(--blue)}
.place-note{left:168px;width:162px;top:178px;text-align:center;font-style:italic;font-size:8.4px;line-height:1.35;color:#222}
.tagline{left:0;width:497px;top:360px;text-align:center;font-style:italic;font-size:19px;color:var(--blue);letter-spacing:-.3px}
.tagline b{color:var(--red);font-weight:700}

.pill{height:25px;line-height:25px;color:#fff;font-style:italic;font-weight:700;font-size:12px;padding-left:22px;border-radius:0 13px 13px 0}
.pill.blue{background:var(--blue)}
.pill.red{background:var(--red)}
.highlights-tag{left:0;top:402px;width:178px}
.performers-tag{left:0;top:507px;width:178px}
.dot-list{list-style:none;font-size:8.4px;line-height:14.3px;color:#222}
.dot-list li{position:relative;padding-left:11px}
.dot-list li::before{content:"";position:absolute;left:1px;top:5.5px;width:4px;height:4px;border-radius:50%;background:var(--red)}
.highlights{left:20px;top:437px;width:240px}
.performers{left:20px;top:541px;width:240px;font-size:9.6px;line-height:12.5px;color:#222}

.study-panel{left:264px;top:393px;width:217px;height:240px;background:var(--panel);border-radius:12px 12px 0 0}
.quote-mark{left:16px;top:6px}
.quote{left:14px;top:10px;width:190px;text-align:center;font-style:italic;font-size:8.2px;line-height:11px;color:#fff}
.quote-name{left:0;top:53px;width:217px;text-align:center;font-size:9.4px;color:var(--red)}
.quote-role{left:0;top:66px;width:217px;text-align:center;font-style:italic;font-size:7.4px;color:var(--muted)}
.study-band{left:0;top:78px;width:217px;height:23px;line-height:23px;text-align:center;background:var(--red);color:#fff;font-style:italic;font-weight:700;font-size:11.5px}
.study-list{left:10px;top:109px;width:200px;color:#f2f2f2;font-size:7.4px;line-height:9.6px}
.study-list li{margin-bottom:4px}
.study-list li::before{top:3.5px}

.brand{font-family:"Open Sans",Arial,sans-serif;font-weight:600;color:var(--red);display:flex;align-items:center;gap:7px;white-space:nowrap}
.brand .mark{display:inline-block;background:var(--red);border-radius:50%}
.front .brand-a{left:24px;top:610px;font-size:21px}
.front .brand-a .mark{width:34px;height:34px}
.front .brand-b{left:26px;top:662px;font-size:14px}
.front .brand-b .mark{width:20px;height:20px}

.footer-band{background:linear-gradient(180deg,var(--red) 0%,var(--red-dark) 100%)}
.front .footer-band{left:236px;top:634px;width:261px;height:68px;border-radius:34px 0 0 0}
.cta{height:26px;line-height:26px;background:#1e1e1f;border-radius:13px;color:#fff;font-style:italic;font-weight:700;font-size:12.5px;text-align:center}
.cta span{color:#ff4a3d}
.front .cta{left:221px;top:622px;width:241px}
.url{display:flex;align-items:center;gap:8px;color:#fff;font-style:italic;font-weight:600;font-size:9.6px;white-space:nowrap}
.front .url-1{left:221px;top:656px}
.front .url-2{left:221px;top:676px}
.url .dot{width:11px;height:11px;border-radius:50%;background:#fff;display:inline-block}

/* back */
.back .brand-a{left:30px;top:20px;font-size:18px}
.back .brand-a .mark{width:34px;height:34px}
.back .brand-b{left:318px;top:30px;font-size:14px}
.back .brand-b .mark{width:18px;height:18px}
.intro{left:30px;top:74px;width:434px;font-size:9.4px;line-height:12.5px;color:#222}
.inclusions-tag{left:0;top:126px;width:169px;height:27px;line-height:27px;background:var(--red);color:#fff;font-weight:700;font-size:13px;padding-left:28px;border-radius:0 14px 14px 0}
.inclusions{left:30px;top:166px;width:233px;list-style:none;font-size:9.2px;line-height:11.8px;color:#222}
.inclusions li{position:relative;padding:0 0 4px 17px;margin-bottom:4px;border-bottom:1px solid var(--rule);text-align:justify}
.inclusions li svg{position:absolute;left:0;top:1px}
.contact{left:46px;top:468px;font-size:9.6px;color:#222}
.contact span{color:var(--red);font-style:italic}
.email{left:46px;top:480px;font-style:italic;font-weight:600;font-size:17px;color:#111}
.col-rule{left:274px;top:150px;width:1px;height:310px;background:#e7e7e7}
.portrait{left:330px;top:142px;width:90px;height:106px;border:2px solid #cfcfcf;border-radius:12px;background:#fff}
.bio{left:289px;top:259px;width:174px;font-size:9.2px;line-height:13.2px;color:#222;text-align:justify}
.bio b{color:var(--red);font-weight:600;font-size:12px}
.shore-photo{left:0;top:505px;width:494px;height:130px;background:linear-gradient(180deg,rgba(255,255,255,1) 0%,#efe3d2 35%,#e3cfb5 100%)}
.back .footer-band{left:0;top:631px;width:494px;height:65px}
.back .cta{left:127px;top:615px;width:240px}
.back .url-1{left:114px;top:652px;font-size:11px}
.back .url-2{left:98px;top:674px;font-size:11px}
</style>
</head>
<body>

<section class="page front">
  <div class="abs hero-photo" role="img" aria-label="Photo of a family running hand in hand along a beach at sunset"></div>
  <div class="abs kicker">Guided Study Tour</div>
  <h1 class="abs title">Halmerfest</h1>
  <div class="abs date">JUNE 12-16, 2019</div>
  <div class="abs place">Leipzig, Germany</div>
  <div class="abs place-note">Plusday trip to Dresden and full day and overnight in Prague</div>

  <p class="abs tagline">Join us for a once in a lifetime .... <b>led by Daniel Marsh....</b></p>

  <div class="abs pill blue highlights-tag">Halmerfest Highlights:</div>
  <ul class="abs dot-list highlights">
    <li>More than 100 Concerts in 42 different Halmer venues</li>
    <li>World Class Musicians &amp; Celebrated Recording Artists</li>
    <li>Day trips to Weimer &amp; Dresden</li>
    <li>Bilingual pre-concert talks &amp; lectures with Halmer Scholars</li>
  </ul>

  <div class="abs pill red performers-tag">Featured Performers:</div>
  <p class="abs performers">Joran Sallet, Tom Kuypers, Cantarion, Leipzig Hallenhaus Orchestra, Silvea, &amp; the Leipzig Stadtchor</p>

  <div class="abs study-panel">
    <svg class="abs quote-mark" width="22" height="16" viewBox="0 0 22 16" aria-hidden="true">
      <circle cx="5" cy="10" r="5" fill="#c8161d"/><path d="M1 9 Q3 2 8 1" stroke="#c8161d" stroke-width="3" fill="none"/>
      <circle cx="16" cy="10" r="5" fill="#c8161d"/><path d="M12 9 Q14 2 19 1" stroke="#c8161d" stroke-width="3" fill="none"/>
    </svg>
    <p class="abs quote">&nbsp;&nbsp;&nbsp;&nbsp;&nbsp;This is where it all has begun...this is why our guests have tears in their eyes istening to the St. Matthew Passion orthe B-Minor Mass</p>
    <div class="abs quote-name">Martin Kohl</div>
    <div class="abs quote-role">Musicologist, Festival Director</div>
    <div class="abs study-band">Study Tour Highlights:</div>
    <ul class="abs dot-list study-list">
      <li>Access to dress rehearsals</li>
      <li>Meet the artist opportunities</li>
      <li>Post-concert discussions led by Daniel Marsh</li>
      <li>Study sessions on Halmer's B-Minor Mass, Magnificat,</li>
      <li>St. John Passion, St. Matthew Passion &amp; Weimar Cantatashours</li>
      <li>Guidance in planning individual concert itinerary</li>
      <li>Professional development or continuing education credit</li>
    </ul>
  </div>

  <div class="abs brand brand-a"><span class="mark"></span>Verner Tours</div>
  <div class="abs brand brand-b"><span class="mark"></span>Crestline Tours</div>

  <div class="abs footer-band"></div>
  <div class="abs cta">Get more <span>Information &amp; Watch Video</span></div>
  <div class="abs url url-1">
    <svg width="11" height="11" viewBox="0 0 12 12" aria-hidden="true"><g fill="none" stroke="#fff" stroke-width="1.1"><circle cx="6" cy="6" r="5.2"/><ellipse cx="6" cy="6" rx="2.3" ry="5.2"/><path d="M1 6h10M2 3.3h8M2 8.7h8"/></g></svg>
    https://www.halmerfest-example.de/en/halmerfest
  </div>
  <div class="abs url url-2"><span class="dot"></span>https://www.videohub-example.com/watch?v=-h4MRtuefd</div>
</section>

<section class="page back">
  <div class="abs brand brand-a"><span class="mark"></span>Verner Tours</div>
  <div class="abs brand brand-b"><span class="mark"></span>Crestline Tours</div>

  <p class="abs intro">Daniel Marsh partnered with Crestline Tours &amp; Music Festivals to bring you and experience of a Lifetime. With over 100 years of combined educational student travel expertise, Crestline Tours, powered by Verner Tours, brings unparalleled tour experiences for you and your students.</p>

  <div class="abs inclusions-tag">TRIP INCLUSIONS</div>
  <ul class="abs inclusions">
    <li><svg width="10" height="10" viewBox="0 0 10 10" aria-hidden="true"><rect x=".5" y="1.5" width="8" height="8" fill="none" stroke="#c8161d"/><path d="M2 5l2 2 5-6" fill="none" stroke="#c8161d" stroke-width="1.4"/></svg>Roundtrip Airfare from Houston</li>
    <li><svg width="10" height="10" viewBox="0 0 10 10" aria-hidden="true"><rect x=".5" y="1.5" width="8" height="8" fill="none" stroke="#c8161d"/><path d="M2 5l2 2 5-6" fill="none" stroke="#c8161d" stroke-width="1.4"/></svg>13 Nights Accomodations, 3 Star Hotels with A/C</li>
    <li><svg width="10" height="10" viewBox="0 0 10 10" aria-hidden="true"><rect x=".5" y="1.5" width="8" height="8" fill="none" stroke="#c8161d"/><path d="M2 5l2 2 5-6" fill="none" stroke="#c8161d" stroke-width="1.4"/></svg>Daily Breakfast</li>
    <li><svg width="10" height="10" viewBox="0 0 10 10" aria-hidden="true"><rect x=".5" y="1.5" width="8" height="8" fill="none" stroke="#c8161d"/><path d="M2 5l2 2 5-6" fill="none" stroke="#c8161d" stroke-width="1.4"/></svg>Access to rehearsal sessions</li>
    <li><svg width="10" height="10" viewBox="0 0 10 10" aria-hidden="true"><rect x=".5" y="1.5" width="8" height="8" fill="none" stroke="#c8161d"/><path d="M2 5l2 2 5-6" fill="none" stroke="#c8161d" stroke-width="1.4"/></svg>Pirvate Luxury Coach Transfer Servicesfor airport transfers and day tours to Berlin, Weimar and Dresden &amp; Prague.</li>
    <li><svg width="10" height="10" viewBox="0 0 10 10" aria-hidden="true"><rect x=".5" y="1.5" width="8" height="8" fill="none" stroke="#c8161d"/><path d="M2 5l2 2 5-6" fill="none" stroke="#c8161d" stroke-width="1.4"/></svg>Professional Local Guides for for City Tours in: Berlin, Weimar, Dresden &amp; Prague</li>
    <li><svg width="10" height="10" viewBox="0 0 10 10" aria-hidden="true"><rect x=".5" y="1.5" width="8" height="8" fill="none" stroke="#c8161d"/><path d="M2 5l2 2 5-6" fill="none" stroke="#c8161d" stroke-width="1.4"/></svg>Entrance Fees to: House of Lukas Brenner, Franz Adler, Hollen in Weimar, Lutheran Frauenkirche&amp; Alte Meister Gallery in the Zwiner Palace in Dresend, and Cathedral and Golden Lane in Prague</li>
    <li><svg width="10" height="10" viewBox="0 0 10 10" aria-hidden="true"><rect x=".5" y="1.5" width="8" height="8" fill="none" stroke="#c8161d"/><path d="M2 5l2 2 5-6" fill="none" stroke="#c8161d" stroke-width="1.4"/></svg>All Applicable Taxes and Gratuities for Included Services, Guides, and Drivers</li>
    <li><svg width="10" height="10" viewBox="0 0 10 10" aria-hidden="true"><rect x=".5" y="1.5" width="8" height="8" fill="none" stroke="#c8161d"/><path d="M2 5l2 2 5-6" fill="none" stroke="#c8161d" stroke-width="1.4"/></svg>$2 Million in Professional Liability Insurance</li>
    <li><svg width="10" height="10" viewBox="0 0 10 10" aria-hidden="true"><rect x=".5" y="1.5" width="8" height="8" fill="none" stroke="#c8161d"/><path d="M2 5l2 2 5-6" fill="none" stroke="#c8161d" stroke-width="1.4"/></svg>24-hour Travel Support Staff</li>
  </ul>

  <div class="abs col-rule"></div>
  <div class="abs portrait" role="img" aria-label="Portrait of the tour leader"></div>
  <p class="abs bio"><b>Daniel Marsh</b> is Director of Choral Studies at Southern Plains University and the conductor of the Plains Symphony Chorale and the Plains Choral Artists, a professional chamber choir. A native Texan, his degrees are from Harlan Pierce University, Bayridge University and the University of Western Meridian. Recent engagements include conducting the Durand Requiem in Buffalo, NY, serving on the jury for the Arvena International Choral Festival in Arvena, Greece and the International Choir Championship Cantabile in Tusnia, Bosnia and Herzogevina.</p>

  <div class="abs shore-photo" role="img" aria-label="Photo of seashells and a starfish on sand"></div>
  <p class="abs contact">For more information contact <span>Dr. Marsh</span> at</p>
  <p class="abs email">daniel.marsh@spu-example.edu</p>

  <div class="abs footer-band"></div>
  <div class="abs cta">Get more <span>Information &amp; Watch Video</span></div>
  <div class="abs url url-1">
    <svg width="14" height="14" viewBox="0 0 12 12" aria-hidden="true"><g fill="none" stroke="#fff" stroke-width="1"><circle cx="6" cy="6" r="5.2"/><ellipse cx="6" cy="6" rx="2.3" ry="5.2"/><path d="M1 6h10M2 3.3h8M2 8.7h8"/></g></svg>
    https://www.halmerfest-example.de/en/halmerfest
  </div>
  <div class="abs url url-2"><span class="dot" style="width:14px;height:14px"></span>https://www.videohub-example.com/watch?v=-h4MRtuefd</div>
</section>

</body>
</html>
```